Coral Ridge Networks Ltd

I need a website that is an informational only. We are a construction business building telecommunications sites. Seeing how our company is Coral Ridge the color blue might want to be incorporated in the color scheme.
I can provide more picture of towers and wireless communications if needed.
current website www.coralridgenet.ca

Industry/Entity Type

Wireless Telecommunications, Construction

Coding

Coded - Design and coding required

Number of Pages Required

2 page

Font styles to use
Sans Serif

Colors

Designer to choose colors to be used in the design.

```html
<!DOCTYPE html>
<html lang="en">
<head>
<meta charset="utf-8">
<title>Coral Ridge Networks Ltd</title>
<link href="https://fonts.googleapis.com/css2?family=Poppins:wght@400;500;600;700&display=swap" rel="stylesheet">
<style>
:root{
  --navy:#283a8f;
  --navy-dark:#22337e;
  --ink:#111318;
  --text:#555a66;
  --muted:#8a8f99;
  --hero-bg:#efefef;
  --card-border:#e4e6ec;
  --soft:#eef0f4;
  --white:#ffffff;
}
*{box-sizing:border-box;margin:0;padding:0}
html,body{width:1200px;height:3983px;overflow:hidden}
body{font-family:'Poppins',sans-serif;color:var(--ink);background:var(--white);position:relative}
.abs{position:absolute}
.wrap{position:absolute;left:85px;width:1029px}

/* top bar */
.topbar{position:absolute;left:85px;top:0;width:1029px;height:46px;background:var(--navy);border-radius:0 0 6px 6px;color:#fff;font-size:14px;font-weight:500;display:flex;align-items:center;padding:0 18px}
.topbar .item{display:flex;align-items:center;gap:10px;margin-right:36px}
.topbar .social{margin-left:auto;display:flex;gap:14px}
.topbar .social span{width:16px;height:16px;border:2px solid #fff;border-radius:50%}

/* header */
.header{position:absolute;left:0;top:46px;width:1200px;height:121px;border-bottom:1px solid #e6e6e6}
.brand{position:absolute;left:85px;top:32px;display:flex;align-items:center;gap:10px;font-size:26px;font-weight:600;color:var(--navy)}
.brand .dot{width:16px;height:16px;background:var(--navy);border-radius:50%}
.nav{position:absolute;left:375px;top:50px;display:flex;gap:30px;font-size:14px;font-weight:500}
.nav a{color:var(--ink);text-decoration:none}
.nav a.active{color:var(--navy)}
.search{position:absolute;left:928px;top:49px}
.btn{display:inline-flex;align-items:center;justify-content:center;gap:8px;background:var(--navy);color:#fff;font-weight:500;font-size:14px;border-radius:3px;text-decoration:none}
.header .btn{position:absolute;left:980px;top:34px;width:134px;height:53px}

/* hero */
.hero{position:absolute;left:0;top:167px;width:1200px;height:563px;background:var(--hero-bg)}
.hero-art{position:absolute;left:0;top:167px;width:1200px;height:611px}
.eyebrow{font-size:15px;font-weight:600;color:var(--navy);text-transform:uppercase}
.hero-copy{position:absolute;left:85px;top:272px;width:460px}
.hero-copy h1{font-size:52px;line-height:63px;font-weight:700;margin-top:6px}
.hero-copy p{font-size:15px;line-height:24px;margin-top:24px;color:#333}
.hero-copy .btn{width:134px;height:53px;margin-top:20px}

/* services */
.center{text-align:center}
.section-title{font-size:36px;font-weight:700;margin-top:6px}
.services-head{position:absolute;left:0;top:893px;width:1200px}
.card{position:absolute;top:1013px;width:327px;height:376px;border:1px solid var(--card-border);border-radius:4px;text-align:center;padding:38px 30px 0;background:#fff}
.card h3{font-size:23px;font-weight:600;margin-top:14px}
.card p{font-size:13px;line-height:20px;color:#333;margin-top:12px}
.card .more{display:inline-flex;align-items:center;gap:8px;height:38px;padding:0 22px;background:var(--soft);font-size:14px;font-weight:500;border-radius:3px;margin-top:20px}
.card.featured{background:linear-gradient(180deg,#e9ebf0,#d9dbe0)}
.card.featured .more{background:#fff}
.accent{position:absolute;left:112px;top:1389px;width:272px;height:18px;background:var(--navy);border-radius:0 0 4px 4px}

/* why */
.why-copy{position:absolute;left:613px;top:1522px;width:501px}
.why-copy h2{font-size:36px;line-height:45px;font-weight:700;margin-top:6px}
.why-copy p{font-size:13px;line-height:22px;color:var(--muted);margin-top:16px}
.ticks{list-style:none;margin-top:16px}
.ticks li{display:flex;align-items:center;gap:12px;font-size:13px;font-weight:500;height:30px}

/* about */
.about{position:absolute;left:0;top:2162px;width:1200px;height:594px;background:linear-gradient(100deg,var(--navy-dark) 0%,#2d48a0 45%,#5e80bf 75%,#a9b9cf 100%);color:#fff}
.about-copy{position:absolute;left:85px;top:115px;width:450px}
.about-copy .eyebrow{color:#fff}
.about-copy h2{font-size:36px;font-weight:700;margin-top:6px}
.about-copy p{font-size:13px;line-height:22px;margin-top:14px;opacity:.95}
.about-copy .outline{display:inline-flex;align-items:center;gap:8px;height:53px;padding:0 28px;border:1px solid #fff;border-radius:3px;margin-top:26px;font-size:14px;font-weight:500}

/* contact */
.contact-head{position:absolute;left:0;top:2862px;width:1200px}
.contact-head p{font-size:13px;line-height:22px;color:var(--muted);margin-top:14px}
.field{position:absolute;height:56px;border:1px solid var(--card-border);border-radius:4px;font-size:13px;color:var(--muted);padding:17px 16px}
.submit{position:absolute;left:532px;top:3227px;width:134px;height:52px}

/* footer */
.footer{position:absolute;left:0;top:3399px;width:1200px;height:584px;background:var(--navy);color:#fff}
.f-logo{position:absolute;left:85px;top:0;width:221px;height:121px;background:#fff;border-radius:0 0 4px 4px;display:flex;align-items:center;justify-content:center;gap:10px;color:var(--navy);font-size:26px;font-weight:600}
.f-logo .dot{width:16px;height:16px;background:var(--navy);border-radius:50%}
.f-info{position:absolute;left:349px;top:0;width:765px;height:121px;background:#ededf0;border-radius:0 0 4px 4px;color:var(--ink);display:flex;align-items:center;padding:0 34px}
.f-info .it{display:flex;gap:16px;align-items:flex-start;flex:1;padding-left:20px;border-left:1px solid #d5d7dd}
.f-info .it:first-child{border-left:0;padding-left:0}
.f-info .ic{width:38px;height:38px;border-radius:50%;background:#fff;display:flex;align-items:center;justify-content:center;flex:none}
.f-info b{font-size:15px;font-weight:600;display:block}
.f-info span{font-size:12px;line-height:20px}
.col{position:absolute;top:202px}
.col h4{font-size:20px;font-weight:600;margin-bottom:22px}
.col a{display:block;color:#fff;text-decoration:none;font-size:13px;font-weight:500;margin-bottom:15px}
.col p{font-size:13px;line-height:22px}
.socials{display:flex;gap:12px;margin-top:24px}
.socials span{width:46px;height:46px;border-radius:50%;background:#fff}
.map{position:absolute;left:876px;top:252px;width:238px;height:181px;border-radius:3px;background:linear-gradient(135deg,#e5ede3,#cfdccb)}
.f-line{position:absolute;left:85px;top:495px;width:1029px;height:1px;background:rgba(255,255,255,.25)}
.f-bottom{position:absolute;left:85px;top:516px;width:1029px;display:flex;justify-content:space-between;font-size:13px}
.f-bottom .accent-text{color:#7fa4ff}
</style>
</head>
<body>

<div class="topbar">
  <div class="item">
    <svg width="16" height="16" viewBox="0 0 24 24" fill="none" stroke="#fff" stroke-width="2"><path d="M22 16.9v3a2 2 0 0 1-2.2 2 19.8 19.8 0 0 1-8.6-3.1 19.5 19.5 0 0 1-6-6A19.8 19.8 0 0 1 2.1 4.2 2 2 0 0 1 4.1 2h3a2 2 0 0 1 2 1.7l.5 3a2 2 0 0 1-.6 1.8L7.6 9.9a16 16 0 0 0 6 6l1.4-1.4a2 2 0 0 1 1.8-.6l3 .5a2 2 0 0 1 1.7 2z"/></svg>
    1-604-555-0148
  </div>
  <div class="item">
    <svg width="18" height="14" viewBox="0 0 24 18" fill="none" stroke="#fff" stroke-width="2"><rect x="1" y="1" width="22" height="16" rx="2"/><path d="M1 2l11 8 11-8"/></svg>
    info@coralridgenet.ca
  </div>
  <div class="social"><span></span><span></span><span></span></div>
</div>

<header class="header">
  <div class="brand"><span class="dot"></span>Coral Ridge</div>
  <nav class="nav">
    <a class="active" href="#">Home</a><a href="#">Services</a><a href="#">About</a><a href="#">Why Choose Us</a><a href="#">Contact Us</a>
  </nav>
  <svg class="search" width="24" height="24" viewBox="0 0 24 24" fill="none" stroke="#111" stroke-width="2"><circle cx="10.5" cy="10.5" r="8"/><path d="M16.5 16.5L22 22"/></svg>
  <a class="btn" href="#">Get Started</a>
</header>

<section class="hero"></section>
<svg class="hero-art" viewBox="0 0 1200 611">
  <defs>
    <linearGradient id="sky" x1="0" y1="0" x2="0" y2="1">
      <stop offset="0" stop-color="#8fb3df"/><stop offset=".45" stop-color="#dfe8f2"/><stop offset="1" stop-color="#f4f6f9"/>
    </linearGradient>
  </defs>
  <polygon points="585,0 640,0 740,611 700,611" fill="#283a8f"/>
  <path d="M632,0 H1200 V611 H730 Q702,611 698,585 Z" fill="url(#sky)" role="img" aria-label="Photo of a telecom tower on a snowy mountain summit"/>
</svg>
<div class="hero-copy">
  <div class="eyebrow">Welcome To</div>
  <h1>Coral Ridge Networks Ltd</h1>
  <p>At Coral Ridge Networks Ltd Safety is number one.</p>
  <a class="btn" href="#">Learn More</a>
</div>

<div class="services-head center">
  <div class="eyebrow">Services We Provide</div>
  <h2 class="section-title">Explore Our Services</h2>
</div>

<div class="card featured" style="left:85px" role="img" aria-label="Rooftop site photo behind card">
  <svg width="44" height="66" viewBox="0 0 44 66" fill="none" stroke="#283a8f" stroke-width="2"><circle cx="22" cy="14" r="3"/><path d="M14 6a11 11 0 0 0 0 16M30 6a11 11 0 0 1 0 16M9 2a17 17 0 0 0 0 24M35 2a17 17 0 0 1 0 24M22 17L10 64M22 17l12 47M15 44h14M12 56h20M16 40l14 16M28 40L14 56"/></svg>
  <h3>Rooftop Sites</h3>
  <p>Structural upgrades or simple ballast mounts. Shelter on the ground, leasehold build outs or cabinets on the roof. Coral Ridge can install what you need where you need it.</p>
  <span class="more">Read More <svg width="16" height="10" viewBox="0 0 16 10" fill="none" stroke="#111" stroke-width="1.5"><path d="M0 5h15M11 1l4 4-4 4"/></svg></span>
</div>
<div class="card" style="left:437px">
  <svg width="66" height="66" viewBox="0 0 66 66" fill="none" stroke="#283a8f" stroke-width="2"><path d="M33 8v56M27 64l6-40 6 40M28 40h10M26 52h14"/><rect x="20" y="18" width="5" height="14"/><rect x="41" y="18" width="5" height="14"/><circle cx="33" cy="8" r="3"/><path d="M10 28a8 8 0 0 1 8-8M52 12a10 10 0 0 1 6 10M4 34h8M54 30h8"/></svg>
  <h3>Towers and Monopoles</h3>
  <p>Coral Ridge can engineer, supply and install all your tower needs. New structures or existing, call us for pricing we would be happy to help out.</p>
  <span class="more">Read More <svg width="16" height="10" viewBox="0 0 16 10" fill="none" stroke="#111" stroke-width="1.5"><path d="M0 5h15M11 1l4 4-4 4"/></svg></span>
</div>
<div class="card" style="left:788px">
  <svg width="66" height="66" viewBox="0 0 66 66" fill="none" stroke="#283a8f" stroke-width="2"><rect x="16" y="6" width="26" height="58"/><path d="M22 14h4M32 14h4M22 22h4M32 22h4M22 30h4M32 30h4M22 38h4M22 46h4M6 64h54"/><rect x="6" y="32" width="10" height="32"/><circle cx="48" cy="48" r="10"/><circle cx="48" cy="48" r="4"/></svg>
  <h3>In Building</h3>
  <p>Small office or large Hotel. Coral Ridge has installed services into all size buildings. Fiber, cat6, or coax, we have the abilities to install, test, and get the job done.</p>
  <span class="more">Read More <svg width="16" height="10" viewBox="0 0 16 10" fill="none" stroke="#111" stroke-width="1.5"><path d="M0 5h15M11 1l4 4-4 4"/></svg></span>
</div>
<div class="accent"></div>

<svg class="abs" style="left:75px;top:1539px" width="480" height="500" viewBox="0 0 480 500">
  <defs>
    <linearGradient id="towerSky" x1="0" y1="0" x2="1" y2="1">
      <stop offset="0" stop-color="#4f6fa8"/><stop offset="1" stop-color="#2f4f8d"/>
    </linearGradient>
  </defs>
  <path d="M100,40 Q250,-20 380,40 Q490,110 470,260 Q450,400 330,440 Q270,460 260,400 Q245,310 150,310 Q60,310 0,330 L0,260 Q0,110 100,40 Z" fill="url(#towerSky)" stroke="#283a8f" stroke-width="6" role="img" aria-label="Photo of a lattice tower with microwave dishes"/>
  <path d="M35,400 Q80,360 120,400 Q160,440 190,380 Q200,450 150,490 Q100,500 60,470 Q25,440 35,400 Z" fill="url(#towerSky)"/>
  <circle cx="88" cy="85" r="82" fill="#fff"/>
  <circle cx="34" cy="85" r="6" fill="#283a8f"/>
  <text x="96" y="93" text-anchor="middle" font-family="Poppins, sans-serif" font-size="22" font-weight="600" fill="#283a8f">Coral Ridge</text>
</svg>
<div class="why-copy">
  <div class="eyebrow">Why Choose Us</div>
  <h2>Coral Ridge Networks Ltd</h2>
  <p>At Coral Ridge Networks Ltd Safety is number one. Coral Ridge Ltd is committed to a strong safety policy, protecting its staff and the general public from accidents and harm. All Coral Ridge Employees are certified "Tower Competent Climber and Rescue".</p>
  <p style="margin-top:12px">In addition to tower safety and fall protection Coral Ridge's safety training and practices include but are not limited to the following:</p>
  <ul class="ticks">
    <li><svg width="14" height="10" viewBox="0 0 14 10" fill="none" stroke="#283a8f" stroke-width="1.6"><path d="M1 5l4 4 8-8"/></svg>COR Certified</li>
    <li><svg width="14" height="10" viewBox="0 0 14 10" fill="none" stroke="#283a8f" stroke-width="1.6"><path d="M1 5l4 4 8-8"/></svg>BC Level 1 first aid</li>
    <li><svg width="14" height="10" viewBox="0 0 14 10" fill="none" stroke="#283a8f" stroke-width="1.6"><path d="M1 5l4 4 8-8"/></svg>Transportation Endorsement first aid</li>
    <li><svg width="14" height="10" viewBox="0 0 14 10" fill="none" stroke="#283a8f" stroke-width="1.6"><path d="M1 5l4 4 8-8"/></svg>Sprat Level 1</li>
    <li><svg width="14" height="10" viewBox="0 0 14 10" fill="none" stroke="#283a8f" stroke-width="1.6"><path d="M1 5l4 4 8-8"/></svg>On site tailboard meeting with daily checklist sign off and picture</li>
    <li><svg width="14" height="10" viewBox="0 0 14 10" fill="none" stroke="#283a8f" stroke-width="1.6"><path d="M1 5l4 4 8-8"/></svg>documentation</li>
    <li><svg width="14" height="10" viewBox="0 0 14 10" fill="none" stroke="#283a8f" stroke-width="1.6"><path d="M1 5l4 4 8-8"/></svg>Monthly in office safety meetings</li>
    <li><svg width="14" height="10" viewBox="0 0 14 10" fill="none" stroke="#283a8f" stroke-width="1.6"><path d="M1 5l4 4 8-8"/></svg>Job site specific hazard assessment and reporting</li>
  </ul>
</div>

<section class="about" role="img" aria-label="Photo of a microwave dish on a steel tower against blue sky">
  <div class="about-copy">
    <div class="eyebrow">About Us</div>
    <h2>Some Words About Us</h2>
    <p>At <b>Coral Ridge Ltd</b>, we are dedicated to providing our customers with friendly professional service. We value your business. We have made it our mission to provide reliable products and services in our customer-driven approach.</p>
    <p>Our courteous, professional team is able to support a range of services to meet your requirements.</p>
    <p>To learn more about <b>Coral Ridge Ltd</b>, and the products and services we can offer, please call us at <b>1-604-555-0148.</b></p>
    <span class="outline">Read More <svg width="16" height="10" viewBox="0 0 16 10" fill="none" stroke="#fff" stroke-width="1.5"><path d="M0 5h15M11 1l4 4-4 4"/></svg></span>
  </div>
</section>

<div class="contact-head center">
  <h2 class="section-title">Contact Us</h2>
  <p>We guarantee high-quality customer support service with high-speed<br>satellite connection all over the world</p>
</div>
<div class="field" style="left:85px;top:2995px;width:335px">Name</div>
<div class="field" style="left:432px;top:2995px;width:335px">Email</div>
<div class="field" style="left:779px;top:2995px;width:335px">Phone</div>
<div class="field" style="left:85px;top:3074px;width:1029px;height:126px">Please tell us your feedback</div>
<a class="btn submit" href="#">Submit Form</a>

<footer class="footer">
  <div class="f-logo"><span class="dot"></span>Coral Ridge</div>
  <div class="f-info">
    <div class="it"><span class="ic"><svg width="16" height="16" viewBox="0 0 24 24" fill="none" stroke="#283a8f" stroke-width="2"><path d="M22 16.9v3a2 2 0 0 1-2.2 2 19.8 19.8 0 0 1-8.6-3.1 19.5 19.5 0 0 1-6-6A19.8 19.8 0 0 1 2.1 4.2 2 2 0 0 1 4.1 2h3a2 2 0 0 1 2 1.7l.5 3a2 2 0 0 1-.6 1.8L7.6 9.9a16 16 0 0 0 6 6l1.4-1.4a2 2 0 0 1 1.8-.6l3 .5a2 2 0 0 1 1.7 2z"/></svg></span><div><b>Call Us:</b><span>1-604-555-0148</span></div></div>
    <div class="it"><span class="ic"><svg width="18" height="14" viewBox="0 0 24 18" fill="none" stroke="#283a8f" stroke-width="2"><rect x="1" y="1" width="22" height="16" rx="2"/><path d="M1 2l11 8 11-8"/></svg></span><div><b>Email:</b><span>info@coralridgenet.ca</span></div></div>
    <div class="it"><span class="ic"><svg width="14" height="18" viewBox="0 0 14 18" fill="none" stroke="#283a8f" stroke-width="1.8"><path d="M7 17s6-6 6-10A6 6 0 0 0 1 7c0 4 6 10 6 10z"/><circle cx="7" cy="7" r="2"/></svg></span><div><b>Location:</b><span>4120 Harbour Ave<br>Westmere, BC V0X 1Z0</span></div></div>
  </div>

  <div class="col" style="left:85px;width:230px">
    <h4>About Us</h4>
    <p>Our courteous, professional team is able to support a range of services to meet your requirements.</p>
    <div class="socials"><span></span><span></span><span></span></div>
  </div>
  <div class="col" style="left:437px">
    <h4>Main Menu</h4>
    <a href="#">Home</a><a href="#">Services</a><a href="#">About</a><a href="#">Why Choose Us</a><a href="#">Contact Us</a>
  </div>
  <div class="col" style="left:648px">
    <h4>Our Services</h4>
    <a href="#">Rooftop Sites</a><a href="#">Towers and Monopoles</a><a href="#">In Building</a>
  </div>
  <div class="col" style="left:876px">
    <h4>Location</h4>
  </div>
  <div class="map" role="img" aria-label="Street map showing the office location"></div>

  <div class="f-line"></div>
  <div class="f-bottom">
    <span>Privacy Policy &nbsp;•&nbsp; Term and Condition</span>
    <span>Copyright 2017 <span class="accent-text">Coral Ridge Ltd</span></span>
  </div>
</footer>

</body>
</html>
```